Modern and sophisticated web design for architect/designer

Lumo Vant is a Building Design & Drafting studio based in Nedlands Western Australia, providing a high quality and complete client service from concept design through Council planning approvals and building licenses to construction drawings for kitchens and bathrooms, extensions, additions, renovations and new homes.

Lumo Vant is looking for a new qwerty design that *is different from a normal* 2/3 column website. The website design must be very arty, clean and catchy. This design needs to be very different and must not look like a downloadable template.

The design must be able to display a lot of photos for the different projects.

The design must comply with W3C standards (i.e. use of fonts) and must be delivered to us in A PSD layered format.

Here are a couple of example website designs that exemplify what I am after:
1) http://www.prtd.com.au/
2) http://www.martinholsbyarchitect.com/en/
3) http://veromiks.com/

I particularly like numbers 1 and 2. The third, Veromiks, jumps around a little between pages as it is actually several companies. I prefer the page design to remain steady if possible.

I like the very clever nature of number 1 (PRTD). It captures the interest, although slightly gimmicky, however I think it doesn't overpower. Its modern, and visual.

I like the clean elegant design of number 2 (Holsby), it simply delivers everything necessary in a clear intelligent manner, its attractive, menu is clever simple to use and attractive.

I would be very happy to have either of these websites.

here is another one:
4) http://www.tqarchitect.com.au/

Although this is similarly elegant, it appears quite dated. I don't like the thumbnails that you click on in the gallery, its quite clumsy. It looks minimalist, and IS minimalist, doesn't look like there is much option to expand other than changing the pictures.

If you look at my own website:
http://www.lumovant.com.au

I designed and built it myself without any skills or experience. I had to use a generic photo album generator which was worse than useless, the point I am trying to make is I tried to make the menu system a little unusual, I tried to keep the pages neat and tidy, and totally used the "black website" method. However I am more inclined to go with the lighter/white pages of (1) and (2) above because they tend to show photos better.

Dear Designers. 

ArtHive Administration has worked to provide a more comprehensive brief. Please review the amended description. 

Kind Regards, Wesley. 

Target Market(s)

Target market is people who are looking to renovate their home

Industry/Entity Type

Construction

Requirements
Must have
• The brief is to design a visual modern, elegant, sophisticated website for a small scale designer/photographer/architect that looks itself like it is designed. Not off the shelf, simple and dated. Basically the design itself has to exemplify me, it has to say "this guy is a designer, and he is good at it".

```html
<!DOCTYPE html>
<html lang="en">
<head>
<meta charset="utf-8">
<title>Lumo Vant — Building Design &amp; Drafting Studio</title>
<link href="https://fonts.googleapis.com/css2?family=Audiowide&family=Rajdhani:wght@500;600&family=Open+Sans:wght@400;600&display=swap" rel="stylesheet">
<style>
:root{
  --page:#d9d9d9;
  --frame:#ffffff;
  --ink:#0e0e0e;
  --bar:#141414;
  --orange:#f26522;
  --blue:#13508f;
  --blue-dark:#0f4679;
  --white:#ffffff;
  --paper:#f6f4f4;
  --text-dark:#1e1e1e;
  --muted:#e6e6e6;
}
*{margin:0;padding:0;box-sizing:border-box}
html,body{width:1073px;height:1200px;overflow:hidden}
body{background:var(--page);font-family:"Open Sans",sans-serif;color:var(--white);position:relative}
.frame{position:absolute;left:85px;top:0;width:896px;height:1200px;background:var(--frame);box-shadow:0 0 6px rgba(0,0,0,.25)}
.site{position:absolute;left:91px;top:0;width:885px;height:1200px;background:var(--ink)}

/* top bar */
.topbar{height:43px;background:var(--bar);display:flex;justify-content:flex-end;align-items:center}
.topbar .tel{font-size:17px;margin-right:18px;letter-spacing:.2px}
.social{display:flex;height:43px}
.social span{width:42px;height:43px;display:block}
.social span:nth-child(odd){background:var(--blue)}
.social span:nth-child(even){background:var(--orange)}

/* nav */
.masthead{display:flex;height:126px}
.brand{width:235px;display:flex;align-items:center;gap:10px;padding-left:14px}
.brand .mark{width:14px;height:14px;background:var(--white)}
.brand .name{font-family:"Audiowide",sans-serif;font-size:20px;letter-spacing:3px;color:var(--white)}
.nav{display:flex;list-style:none}
.nav li{display:flex;flex-direction:column;align-items:center;justify-content:center;background:var(--blue);border-left:1px solid var(--blue-dark)}
.nav li.current{background:var(--orange);border-left:none}
.nav .label{font-family:"Audiowide",sans-serif;font-size:19px}
.nav .sub{font-size:11.5px;margin-top:8px}

/* hero */
.hero{position:relative;height:362px;display:flex;background:#050505}
.hero-photo{width:442px;height:340px;background:linear-gradient(160deg,#6b5a4e 0%,#3c2c24 45%,#8a4a2a 75%,#2a1a12 100%)}
.hero-copy{flex:1;text-align:right;padding:78px 44px 0 0}
.hero-copy h1{font-family:"Audiowide",sans-serif;font-weight:400;font-size:30px;line-height:40px;text-transform:uppercase}
.hero-copy h1 em{font-style:normal;color:var(--orange)}
.hero-copy p{margin-top:22px;font-size:15px;line-height:23px;letter-spacing:.3px}
.slider-bar{position:absolute;left:0;bottom:0;width:885px;height:22px;background:#0a0a0a;display:flex;align-items:center;justify-content:center;gap:8px;padding-right:22px}
.slider-bar .dot{width:12px;height:12px;background:var(--white)}
.slider-bar .dot.on{background:var(--orange)}
.slider-bar svg{margin:0 22px}

/* project grid */
.projects{display:grid;grid-template-columns:repeat(4,221.25px);grid-template-rows:221px 221px}
.photo{display:block}
.tile{display:flex;flex-direction:column;align-items:center;justify-content:center}
.tile.orange{background:var(--orange)}
.tile.blue{background:var(--blue)}
.tile h2{font-family:"Rajdhani",sans-serif;font-weight:500;font-size:36px;line-height:36px}
.tile span{font-size:16px;margin-top:6px}
.mosaic{display:grid;grid-template-columns:1fr 1fr;grid-template-rows:1fr 1fr}
.intro{background:var(--paper);color:var(--text-dark);padding:22px 20px 0 26px}
.intro h2{font-family:"Rajdhani",sans-serif;font-weight:500;font-size:36px;line-height:36px}
.intro p{font-size:11.5px;line-height:17.7px;margin-top:12px}
.btn{margin-top:15px;width:179px;height:32px;background:var(--orange);display:flex;align-items:center;justify-content:space-between;padding-left:12px;color:var(--white);font-family:"Rajdhani",sans-serif;font-size:18px;font-weight:500}
.btn i{width:32px;height:32px;display:flex;align-items:center;justify-content:center;border-left:1px solid #c94d14}

/* footer */
.footer{border-top:4px solid var(--orange);height:187px;background:#111;display:grid;grid-template-columns:repeat(4,221.25px)}
.footer .col{padding:0 16px 0 17px}
.footer h3{font-family:"Rajdhani",sans-serif;font-weight:500;font-size:19px;height:35px;line-height:40px;margin:0 -16px 0 -17px;padding-left:17px;background:#0c0c0c}
.footer ul{list-style:none;margin-top:12px;padding-left:5px}
.footer li{font-size:11px;line-height:19.5px}
.footer p{font-size:11px;line-height:17.7px;margin-top:10px}
.signup{display:flex;margin-top:12px}
.signup .field{width:156px;height:33px;background:var(--white);color:#444;font-style:italic;font-size:11px;display:flex;align-items:center;padding-left:16px}
.signup .go{width:34px;height:33px;background:var(--blue);display:flex;align-items:center;justify-content:center}
.contact p{margin-top:14px;font-size:11px;line-height:16px}
.contact .links{display:flex;gap:4px;margin-top:8px}
.contact .links span{width:21px;height:21px;background:var(--blue)}
.legal{height:41px;background:#1b1b1b;text-align:center;font-size:9px;line-height:41px;color:var(--muted)}
</style>
</head>
<body>
<div class="frame"></div>
<div class="site">
  <header class="topbar">
    <span class="tel">Tel : &nbsp;+44(0) 20946 31785</span>
    <nav class="social" aria-label="Social channels">
      <span></span><span></span><span></span><span></span><span></span><span></span>
    </nav>
  </header>

  <div class="masthead">
    <div class="brand"><span class="mark"></span><span class="name">LUMO VANT</span></div>
    <ul class="nav">
      <li class="current" style="width:122px"><span class="label">Home</span></li>
      <li style="width:127px"><span class="label">About us</span><span class="sub">Who we are</span></li>
      <li style="width:141px"><span class="label">Services</span><span class="sub">What we do</span></li>
      <li style="width:129px"><span class="label">Projects</span><span class="sub">What we have made</span></li>
      <li style="width:131px"><span class="label">Contact</span><span class="sub">Keep in touch</span></li>
    </ul>
  </div>

  <section class="hero">
    <div class="hero-photo" role="img" aria-label="Photo of a modern kitchen with timber floor and warm lighting"></div>
    <div class="hero-copy">
      <h1>Building <em>Design</em> &amp;<br>Drafting Studio</h1>
      <p>“Providing a high quality and complete client service from concept design through Council planning approvals and building licenses to construction drawings for kitchens and bathrooms, extensions, additions, renovations and new homes.”</p>
    </div>
    <div class="slider-bar">
      <svg width="8" height="10" viewBox="0 0 8 10"><path d="M7 0 L0 5 L7 10Z" fill="#fff"/></svg>
      <span class="dot"></span><span class="dot on"></span><span class="dot"></span><span class="dot"></span>
      <svg width="8" height="10" viewBox="0 0 8 10"><path d="M1 0 L8 5 L1 10Z" fill="#fff"/></svg>
    </div>
  </section>

  <section class="projects">
    <div class="photo" role="img" aria-label="Photo of a timber deck with outdoor dining at dusk" style="background:linear-gradient(170deg,#7c8c8e 0%,#3d3f33 45%,#3a2418 100%)"></div>
    <div class="tile orange"><h2>PROJECTS</h2><span>Project Name</span></div>
    <div class="photo" role="img" aria-label="Photo of a stone-clad house lit up at night" style="background:linear-gradient(170deg,#23324a 0%,#5a4a2c 55%,#1e2416 100%)"></div>
    <div class="tile blue"><h2>PROJECTS</h2><span>Project Name</span></div>
    <div class="photo" role="img" aria-label="Photo of a two-storey house with large glazed walls" style="background:linear-gradient(170deg,#4f86d0 0%,#a6b2bf 50%,#6a6a5c 100%)"></div>
    <div class="tile blue"><h2>PROJECTS</h2><span>Project Name</span></div>
    <div class="mosaic">
      <div role="img" aria-label="Photo of a curved glass interior" style="background:linear-gradient(160deg,#6d7c9a,#1c2230)"></div>
      <div role="img" aria-label="Photo of a timber deck at dusk" style="background:linear-gradient(170deg,#7c8c8e,#3a2418)"></div>
      <div role="img" aria-label="Photo of a glazed two-storey house" style="background:linear-gradient(170deg,#4f86d0,#6a6a5c)"></div>
      <div role="img" aria-label="Photo of a stone house at night" style="background:linear-gradient(170deg,#23324a,#5a4a2c)"></div>
    </div>
    <div class="intro">
      <h2>PROJECTS</h2>
      <p>Lorem ipsum dolor sit amet, consectetur adipiscing elit. Duis laoreet pulvinar est, at vestibu-lum nibh varius ac. Phasellus placerat ante metus, a porttitor.</p>
      <div class="btn">View all projects<i><svg width="18" height="16" viewBox="0 0 18 16"><rect x="1" y="1" width="16" height="14" fill="none" stroke="#fff" stroke-width="2"/><path d="M4 8 H13 M9 4 L13 8 L9 12" fill="none" stroke="#fff" stroke-width="2"/></svg></i></div>
    </div>
  </section>

  <footer class="footer">
    <div class="col">
      <h3>Quick Links</h3>
      <ul><li>Council planning approvals</li><li>Construction drawings</li><li>Extensions</li><li>Building licenses</li><li>Renovations and new homes</li></ul>
    </div>
    <div class="col">
      <h3>Quick Links</h3>
      <ul><li>Contact us</li><li>Site map</li><li>Cookie policy</li></ul>
    </div>
    <div class="col">
      <h3>Start Designing</h3>
      <p>Do you have a project that need designing? Fill out your phone number below and we will call you. Start your project today</p>
      <div class="signup">
        <span class="field">Phone number</span>
        <span class="go"><svg width="18" height="18" viewBox="0 0 18 18"><circle cx="9" cy="9" r="7.5" fill="none" stroke="#fff" stroke-width="1.5"/><path d="M5 9 H12 M9 6 L12 9 L9 12" fill="none" stroke="#fff" stroke-width="1.5"/></svg></span>
      </div>
    </div>
    <div class="col contact">
      <h3>Keep in Touch</h3>
      <p>100 Street Name,<br>State, Country<br>Zipcode<br>tel: +44(0) 20946 31785<br>info@lumovantdesign.com</p>
      <div class="links" aria-label="Social channels"><span></span><span></span><span></span></div>
    </div>
  </footer>
  <div class="legal">Copyright © 2013 Lumo Vant. Use of this website constitutes acceptance of our User Agreement and Privacy Policy.</div>
</div>
</body>
</html>
```